Brennick Holdings Business Cards

These are professional business cards that are for my family office.
Put fake emails and phone numbers as of now until I finalize those components. This family office controls my families investments, assets, and future. The cards should be professional.
..
.
.
.
I just uploaded another variation of a logo I would like to see as a business card to I am inbeteen which logo to use

Target Market(s)

business

Industry/Entity Type

business

Contact Information for Business Card

Professional, wealth related, finance related.

Requirements
Must have
• Logo

```html
<!DOCTYPE html>
<html lang="en">
<head>
<meta charset="utf-8">
<title>Brennick Holdings Business Cards</title>
<link rel="stylesheet" href="https://fonts.googleapis.com/css2?family=Lato:wght@300&family=Playfair+Display:wght@400&family=Raleway:wght@400;500&display=swap">
<style>
  :root {
    --page: #ffffff;
    --card: #f2f2f4;
    --ink: #0b0b0d;
    --gold: #c6ad6e;
  }
  * { margin: 0; padding: 0; box-sizing: border-box; }
  html, body {
    width: 1200px;
    height: 1200px;
    overflow: hidden;
    background: var(--page);
  }
  .card {
    position: absolute;
    left: 197px;
    width: 805px;
    height: 460px;
    background: var(--card);
  }
  .card--front { top: 106px; }
  .card--back { top: 680px; }

  .identity {
    position: absolute;
    right: 71px;
    top: 100px;
    text-align: right;
  }
  .identity__name {
    font-family: "Raleway", sans-serif;
    font-weight: 500;
    font-size: 47px;
    line-height: 1;
    color: var(--ink);
    letter-spacing: -0.2px;
  }
  .identity__role {
    margin-top: 12px;
    font-family: "Raleway", sans-serif;
    font-weight: 400;
    font-size: 19px;
    line-height: 1;
    color: var(--gold);
  }
  .identity__rule {
    margin: 11px 0 0 auto;
    width: 169px;
    height: 2px;
    background: var(--gold);
  }

  .contacts {
    position: absolute;
    right: 71px;
    top: 298px;
    list-style: none;
  }
  .contacts__item {
    display: flex;
    align-items: center;
    justify-content: flex-end;
    height: 31px;
    font-family: "Lato", sans-serif;
    font-weight: 300;
    font-size: 25px;
    color: var(--gold);
  }
  .contacts__icon {
    width: 15px;
    height: 15px;
    margin-left: 16px;
    fill: var(--gold);
  }

  .brand-mark {
    position: absolute;
    left: 81px;
    display: flex;
    align-items: center;
  }
  .card--front .brand-mark { top: 339px; }
  .card--back .brand-mark { top: 351px; }
  .brand-mark__square {
    width: 14px;
    height: 14px;
    background: var(--gold);
    margin-right: 10px;
  }
  .brand-mark__name {
    font-family: "Playfair Display", serif;
    font-size: 18px;
    letter-spacing: 1px;
    color: var(--ink);
    text-transform: uppercase;
  }

  .wordmark {
    position: absolute;
    right: 73px;
    top: 333px;
    font-family: "Playfair Display", serif;
    font-weight: 400;
    font-size: 38px;
    line-height: 1;
    letter-spacing: 1px;
    color: var(--ink);
    text-transform: uppercase;
  }
</style>
</head>
<body>
  <section class="card card--front">
    <div class="identity">
      <h1 class="identity__name">Elena Marsh</h1>
      <p class="identity__role">Managing Director</p>
      <div class="identity__rule"></div>
    </div>

    <div class="brand-mark">
      <span class="brand-mark__square"></span>
      <span class="brand-mark__name">Brennick Holdings</span>
    </div>

    <ul class="contacts">
      <li class="contacts__item">07700 900418
        <svg class="contacts__icon" viewBox="0 0 16 16" aria-hidden="true"><path d="M3.6 1.2l2.2 2.4c.4.4.4 1 0 1.4L4.7 6.1c.8 2 2.6 3.9 4.8 4.9l1.1-1.2c.4-.4 1-.4 1.4 0l2.3 2.2c.4.4.4 1 0 1.4l-1.2 1.2c-.7.7-1.8.9-2.7.5C6.1 13.5 2.6 10 1 5.6.7 4.7.9 3.7 1.6 3l1.2-1.1c.3-.3.6-.9.8-.7z"/></svg>
      </li>
      <li class="contacts__item">brennickholdings@mail.com
        <svg class="contacts__icon" viewBox="0 0 16 16" aria-hidden="true"><path d="M1 3h14v10H1z M2.4 4.2l5.6 4.6 5.6-4.6v.9L8 9.8 2.4 5.1z M2.4 11.8l4-3.4.6.5-3.6 2.9z M13.6 11.8l-4-3.4-.6.5 3.6 2.9z" fill-rule="evenodd"/></svg>
      </li>
      <li class="contacts__item">brennickholdings.com
        <svg class="contacts__icon" viewBox="0 0 16 16" aria-hidden="true"><path d="M2 1l11 5.5-4.6 1.3 4.4 5.2-1.6 1.4-4.4-5.3L4 13z"/></svg>
      </li>
    </ul>
  </section>

  <section class="card card--back">
    <div class="brand-mark">
      <span class="brand-mark__square"></span>
      <span class="brand-mark__name">Brennick Holdings</span>
    </div>
    <p class="wordmark">Brennick Holdings</p>
  </section>
</body>
</html>
```